Tights Color Chart

We Need for a Webshop 3 or 4 different Color Charts to see the Colors of the Tights.

1 Color Chart only with this Colors: black/schwarz, white/weiss,
naturel/natur.

The other 3 or 4 Charts up to your Design!

Total 54 Colors.

The Language must be in English and German.
Each single Color Chart should have rounded Corners see attachment.

Thank you in advance
TOM

Target Market(s)

Woman, Webshop

Requirements
Must have
• the right Colors, English and German, for the Webshop

```html
<!DOCTYPE html>
<html lang="en">
<head>
<meta charset="utf-8">
<title>Tights Colour Chart</title>
<link rel="stylesheet" href="https://fonts.googleapis.com/css2?family=Noto+Sans:wght@400;700&display=swap">
<style>
  :root {
    --page-bg: #ffffff;
    --ink: #111111;
    --swatch-w: 69px;
    --swatch-h: 46px;
    --swatch-radius: 11px;
    --row-pitch: 89.5px;
  }
  html, body {
    margin: 0;
    padding: 0;
    width: 1200px;
    height: 2571px;
    overflow: hidden;
    background: var(--page-bg);
  }
  .chart {
    position: absolute;
    left: 367px;
    top: 94px;
    display: grid;
    grid-template-columns: 140px 140px 140px;
    column-gap: 11px;
    align-items: start;
    font-family: "Noto Sans", Verdana, sans-serif;
    color: var(--ink);
  }
  .chart__column {
    display: grid;
    grid-auto-rows: var(--row-pitch);
  }
  .colour {
    display: flex;
    flex-direction: column;
    align-items: center;
    text-align: center;
  }
  .colour__swatch {
    width: var(--swatch-w);
    height: var(--swatch-h);
    border-radius: var(--swatch-radius);
    background: linear-gradient(90deg, var(--from), var(--to));
  }
  .colour__en {
    margin-top: 12px;
    font-size: 13.5px;
    font-weight: 700;
    line-height: 1;
  }
  .colour__de {
    margin-top: 1px;
    font-size: 12.5px;
    font-weight: 400;
    line-height: 1;
  }
</style>
</head>
<body>
<main class="chart">
  <section class="chart__column">
    <div class="colour"><div class="colour__swatch" style="--from:#c9c9c9;--to:#ffffff"></div><span class="colour__en">white</span><span class="colour__de">weiss</span></div>
    <div class="colour"><div class="colour__swatch" style="--from:#c8cac4;--to:#f4f6ee"></div><span class="colour__en">cream</span><span class="colour__de">creme</span></div>
    <div class="colour"><div class="colour__swatch" style="--from:#cbcbc6;--to:#fbfbf2"></div><span class="colour__en">kalina</span><span class="colour__de">kalina</span></div>
    <div class="colour"><div class="colour__swatch" style="--from:#c5c9c5;--to:#f2f7ef"></div><span class="colour__en">ecru</span><span class="colour__de">ecru</span></div>
    <div class="colour"><div class="colour__swatch" style="--from:#c6c6c0;--to:#ecece4"></div><span class="colour__en">perle</span><span class="colour__de">perle</span></div>
    <div class="colour"><div class="colour__swatch" style="--from:#b7b7b9;--to:#e0e0e0"></div><span class="colour__en">ash</span><span class="colour__de">asche</span></div>
    <div class="colour"><div class="colour__swatch" style="--from:#7b6565;--to:#9b8282"></div><span class="colour__en">cacao</span><span class="colour__de">kakao</span></div>
    <div class="colour"><div class="colour__swatch" style="--from:#72584b;--to:#8d6e5e"></div><span class="colour__en">nugat</span><span class="colour__de">novgat</span></div>
    <div class="colour"><div class="colour__swatch" style="--from:#8c6750;--to:#b48c6c"></div><span class="colour__en">beige</span><span class="colour__de">beige</span></div>
    <div class="colour"><div class="colour__swatch" style="--from:#9a7a6c;--to:#c9a48f"></div><span class="colour__en">naturel</span><span class="colour__de">natur</span></div>
    <div class="colour"><div class="colour__swatch" style="--from:#b06d68;--to:#e2928a"></div><span class="colour__en">salmon</span><span class="colour__de">lachs</span></div>
    <div class="colour"><div class="colour__swatch" style="--from:#b86a28;--to:#ee8e30"></div><span class="colour__en">orange</span><span class="colour__de">orange</span></div>
    <div class="colour"><div class="colour__swatch" style="--from:#943a3a;--to:#c34a4a"></div><span class="colour__en">rosso</span><span class="colour__de">rosso</span></div>
    <div class="colour"><div class="colour__swatch" style="--from:#8e3443;--to:#bb4555"></div><span class="colour__en">lipstic</span><span class="colour__de">rot</span></div>
    <div class="colour"><div class="colour__swatch" style="--from:#b0384a;--to:#e4505e"></div><span class="colour__en">sorbet</span><span class="colour__de">sorbet</span></div>
    <div class="colour"><div class="colour__swatch" style="--from:#b63c62;--to:#e05279"></div><span class="colour__en">raspberry</span><span class="colour__de">himbeer</span></div>
    <div class="colour"><div class="colour__swatch" style="--from:#bb6a97;--to:#e78cbb"></div><span class="colour__en">orchidea</span><span class="colour__de">orchidea</span></div>
    <div class="colour"><div class="colour__swatch" style="--from:#c77fa8;--to:#fba4d3"></div><span class="colour__en">pink</span><span class="colour__de">rosa</span></div>
    <div class="colour"><div class="colour__swatch" style="--from:#bda3ad;--to:#f2d5e0"></div><span class="colour__en">rose</span><span class="colour__de">hellrosa</span></div>
    <div class="colour"><div class="colour__swatch" style="--from:#c8c2c6;--to:#fff6fb"></div><span class="colour__en">baby pink</span><span class="colour__de">baby rosa</span></div>
    <div class="colour"><div class="colour__swatch" style="--from:#b03f8a;--to:#df5cb4"></div><span class="colour__en">crocus</span><span class="colour__de">krokus</span></div>
    <div class="colour"><div class="colour__swatch" style="--from:#9e3f72;--to:#c85591"></div><span class="colour__en">lavende</span><span class="colour__de">lavendel</span></div>
    <div class="colour"><div class="colour__swatch" style="--from:#83315f;--to:#a8417b"></div><span class="colour__en">fuchsia</span><span class="colour__de">fuchsia</span></div>
    <div class="colour"><div class="colour__swatch" style="--from:#6f3152;--to:#934269"></div><span class="colour__en">mulberry</span><span class="colour__de">maulbeere</span></div>
    <div class="colour"><div class="colour__swatch" style="--from:#6e3f80;--to:#955aa7"></div><span class="colour__en">azalea</span><span class="colour__de">azalea</span></div>
    <div class="colour"><div class="colour__swatch" style="--from:#6d5a9a;--to:#9c7dc5"></div><span class="colour__en">iris</span><span class="colour__de">iris</span></div>
    <div class="colour"><div class="colour__swatch" style="--from:#a495b5;--to:#d4c0ec"></div><span class="colour__en">lila</span><span class="colour__de">lila</span></div>
  </section>
  <section class="chart__column">
    <div class="colour"><div class="colour__swatch" style="--from:#763459;--to:#98466e"></div><span class="colour__en">violet</span><span class="colour__de">violett</span></div>
    <div class="colour"><div class="colour__swatch" style="--from:#744856;--to:#946472"></div><span class="colour__en">prugna</span><span class="colour__de">pflaume</span></div>
    <div class="colour"><div class="colour__swatch" style="--from:#634659;--to:#836578"></div><span class="colour__en">berry</span><span class="colour__de">beerch</span></div>
    <div class="colour"><div class="colour__swatch" style="--from:#543636;--to:#724d4a"></div><span class="colour__en">bronzo</span><span class="colour__de">bronze</span></div>
    <div class="colour"><div class="colour__swatch" style="--from:#474728;--to:#5f5c34"></div><span class="colour__en">olive</span><span class="colour__de">olive</span></div>
    <div class="colour"><div class="colour__swatch" style="--from:#bccd85;--to:#ecffa5"></div><span class="colour__en">kiwi</span><span class="colour__de">kiwi</span></div>
    <div class="colour"><div class="colour__swatch" style="--from:#5ea663;--to:#86dc88"></div><span class="colour__en">verde</span><span class="colour__de">grün</span></div>
    <div class="colour"><div class="colour__swatch" style="--from:#2f8641;--to:#48ad58"></div><span class="colour__en">grass</span><span class="colour__de">grassgrün</span></div>
    <div class="colour"><div class="colour__swatch" style="--from:#86c0ad;--to:#b1f2dc"></div><span class="colour__en">aquamarina</span><span class="colour__de">aquamarina</span></div>
    <div class="colour"><div class="colour__swatch" style="--from:#22a692;--to:#34d0b9"></div><span class="colour__en">lagoon</span><span class="colour__de">lagune</span></div>
    <div class="colour"><div class="colour__swatch" style="--from:#44a4a1;--to:#6adcd8"></div><span class="colour__en">lazur</span><span class="colour__de">lazur</span></div>
    <div class="colour"><div class="colour__swatch" style="--from:#22a7b3;--to:#34d3df"></div><span class="colour__en">turquoise</span><span class="colour__de">türkis</span></div>
    <div class="colour"><div class="colour__swatch" style="--from:#8ea8c0;--to:#c0dcf5"></div><span class="colour__en">blue</span><span class="colour__de">blau</span></div>
    <div class="colour"><div class="colour__swatch" style="--from:#46466c;--to:#5a5a88"></div><span class="colour__en">baby blue</span><span class="colour__de">baby blau</span></div>
    <div class="colour"><div class="colour__swatch" style="--from:#3c5068;--to:#54708e"></div><span class="colour__en">jeans</span><span class="colour__de">jeans</span></div>
    <div class="colour"><div class="colour__swatch" style="--from:#33324a;--to:#434260"></div><span class="colour__en">ocean</span><span class="colour__de">ozean</span></div>
    <div class="colour"><div class="colour__swatch" style="--from:#2d3142;--to:#3c4158"></div><span class="colour__en">night</span><span class="colour__de">nacht</span></div>
    <div class="colour"><div class="colour__swatch" style="--from:#3a2c48;--to:#4d3b5e"></div><span class="colour__en">blu marino</span><span class="colour__de">blu marino</span></div>
    <div class="colour"><div class="colour__swatch" style="--from:#423a5a;--to:#584e76"></div><span class="colour__en">blu marino melange</span><span class="colour__de">blu marino melange</span></div>
    <div class="colour"><div class="colour__swatch" style="--from:#342a3c;--to:#463850"></div><span class="colour__en">denim</span><span class="colour__de">denim</span></div>
    <div class="colour"><div class="colour__swatch" style="--from:#474b4a;--to:#5c6260"></div><span class="colour__en">silver</span><span class="colour__de">silber</span></div>
    <div class="colour"><div class="colour__swatch" style="--from:#6b5a6a;--to:#8a7688"></div><span class="colour__en">steel</span><span class="colour__de">stahl</span></div>
    <div class="colour"><div class="colour__swatch" style="--from:#4c3f44;--to:#63535a"></div><span class="colour__en">gray</span><span class="colour__de">grau</span></div>
    <div class="colour"><div class="colour__swatch" style="--from:#4a4040;--to:#625656"></div><span class="colour__en">graphite</span><span class="colour__de">graphit</span></div>
    <div class="colour"><div class="colour__swatch" style="--from:#3c3d3c;--to:#525352"></div><span class="colour__en">smoke</span><span class="colour__de">rauch</span></div>
    <div class="colour"><div class="colour__swatch" style="--from:#323232;--to:#444444"></div><span class="colour__en">nero</span><span class="colour__de">schwarz</span></div>
    <div class="colour"><div class="colour__swatch" style="--from:#333333;--to:#454545"></div><span class="colour__en">nero melange</span><span class="colour__de">schwart melange</span></div>
  </section>
  <section class="chart__column">
    <div class="colour"><div class="colour__swatch" style="--from:#c9c9c9;--to:#ffffff"></div><span class="colour__en">white</span><span class="colour__de">weiss</span></div>
    <div class="colour"><div class="colour__swatch" style="--from:#000000;--to:#000000"></div><span class="colour__en">black</span><span class="colour__de">schwarz</span></div>
    <div class="colour"><div class="colour__swatch" style="--from:#d2cabc;--to:#fff6e4"></div><span class="colour__en">nature</span><span class="colour__de">natur</span></div>
  </section>
</main>
</body>
</html>
```